Fizz Bam Dishwasher Cleaner Label

Fizz Bam has a new dishwasher cleaning product. We are looking for a new label. We want to keep our Fizz Bam logo but have designers come up with ideas for the label. We are also interested in color ideas for our logo (like Brava Fizz is red, KLT is brown, Hartwell arches, etc.) This label will part of our new line of products, washing machine cleaner, spot/stain remover, dishwasher cleaner, hot tub cleaner. We sell our Fizz Bam jetted tub cleaner on Vendora. We would like the label to have the quality and look to help us get into stores.

We are open to creative ideas. Consumers should be able to recognize that the label is for a dishwasher cleaner.

Target Market(s)

Consumers

Industry/Entity Type

Cleaning Product

Font styles to use
Sans Serif

Requirements
Must have
• Must use out Fizz Bam logo. You can come up with a new color or keep the same color. We are open to ideas.
• This is a label for our Dishwasher Cleaner only
• We want the logo to be centered on the label.
• The label dimensions are 5" high x 7.5" wide
• The visible area of the front of the label is 5" high x 3.5" wide
• The bottle is a clear bullet, 2.5" diameter and 8" high.
Nice to have
• should have a professional look for the label that will help us get onto store shelves.
Should not have
• Clip art

```html
<!DOCTYPE html>
<html lang="en">
<head>
<meta charset="utf-8">
<title>Fizz Bam Dishwasher Cleaner Label</title>
<link rel="stylesheet" href="https://fonts.googleapis.com/css2?family=Montserrat:wght@500;700;800;900&display=swap">
<style>
  :root {
    --page: #ffffff;
    --navy-deep: #071a5c;
    --navy: #0d2d8f;
    --royal: #1a4fc4;
    --sky: #7fb6ff;
    --ice: #d8ecff;
    --logo-yellow: #ffe600;
    --strip-yellow: #fff200;
    --strip-green: #39b54a;
    --white: #ffffff;
    --ink-blue: #0b2a7a;
  }
  * { box-sizing: border-box; margin: 0; padding: 0; }
  html, body {
    width: 831px; height: 1200px; overflow: hidden;
    background: var(--page);
    font-family: "Montserrat", Arial, sans-serif;
  }
  .canvas {
    position: relative; width: 831px; height: 1200px;
  }
  .label {
    position: absolute; left: 65px; top: 100px;
    width: 700px; height: 1000px;
    background: linear-gradient(180deg, var(--navy-deep) 0%, var(--navy) 45%, var(--navy-deep) 100%);
    overflow: hidden;
  }
  .hero-visual {
    position: absolute; inset: 0 0 150px 0;
    background:
      radial-gradient(ellipse at 62% 38%, rgba(216,236,255,0.85) 0%, rgba(127,182,255,0.45) 22%, rgba(26,79,196,0.2) 48%, transparent 70%),
      radial-gradient(ellipse at 30% 70%, rgba(200,225,255,0.55) 0%, rgba(26,79,196,0.15) 35%, transparent 60%),
      linear-gradient(180deg, var(--navy-deep), var(--navy) 60%, var(--navy-deep));
  }
  .brand-name {
    position: absolute; left: 40px; top: 110px;
    font-weight: 900; font-size: 96px; line-height: 0.95;
    color: var(--logo-yellow);
    letter-spacing: -1px;
  }
  .product-badge {
    position: absolute; left: 410px; top: 400px;
    width: 210px; height: 210px; border-radius: 50%;
    background: radial-gradient(circle at 40% 35%, var(--royal), var(--navy-deep));
    border: 4px solid var(--white);
    display: flex; flex-direction: column; align-items: center; justify-content: center;
    color: var(--white); text-align: center;
  }
  .product-badge .type { font-weight: 700; font-size: 24px; }
  .product-badge .kind { font-weight: 800; font-size: 28px; letter-spacing: 1px; margin-top: 4px; }
  .tagline {
    position: absolute; left: 430px; top: 650px;
    color: var(--white); font-weight: 700; font-size: 44px; line-height: 1.15;
  }
  .volume {
    position: absolute; right: 0; top: 850px;
    width: 300px; height: 40px;
    background: var(--royal);
    color: var(--white); font-weight: 700; font-size: 20px;
    display: flex; align-items: center; justify-content: center;
  }
  .caution-strip {
    position: absolute; left: 0; top: 870px;
    width: 400px; height: 60px;
    background: var(--strip-yellow);
    color: var(--ink-blue); font-weight: 500; font-size: 13px; line-height: 1.4;
    padding: 12px 24px;
  }
  .info-strip {
    position: absolute; left: 0; right: 0; bottom: 0;
    height: 70px;
    background: var(--strip-green);
    color: var(--white); font-weight: 500; font-size: 13px; line-height: 1.4;
    padding: 18px 24px 0 420px;
  }
</style>
</head>
<body>
<main class="canvas">
  <section class="label">
    <div class="hero-visual" role="img" aria-label="Sparkling clean wine glass, fork and knife in cool blue light"></div>
    <div class="brand-name">Fizz<br>Bam</div>
    <div class="product-badge">
      <span class="type">Dishwasher</span>
      <span class="kind">CLEANER</span>
    </div>
    <p class="tagline">Perfect<br>Clean<br>Wash</p>
    <div class="volume">16 fl. oz. | 473 ml</div>
    <div class="caution-strip">Keep out of reach of children.<br>Use once a month.</div>
    <div class="info-strip">Recycle this bottle after use.<br>Made in the USA.</div>
  </section>
</main>
</body>
</html>
```